Business Card for Financial Asset Management Company

Now we are launching a new company based in Tokyo.
The company information is below;

Company Name: Talvane Management

Operations: Financial assets management, Proposing forming portfolio of assets, Consulting service, and advising to enhance your company's financial health

Corporate Colour: Japan Blue or Navy like below
http://staffpages.qorvenly.edu/mtavis/images/Slate/Teal-Slate-217.jpg

It's dark and deep, and will get to fit to our clients as our relationships last longer and longer.

Our images for this colour are "Japanese style" and "pride in our craftmanship" , and also "gentle".

Corporate Key Image: an order taker who is sincere, polite, but courageous

We don't have our logo yet so please feel free to put any symbol on your design.

Please do not hesitate about asking any questions.
Thank you :-)

Reason: We are still discussin on final decision. Thank you for your understanding.

```html
<!DOCTYPE html>
<html lang="en">
<head>
<meta charset="utf-8">
<title>Talvane Management – Business Card</title>
<link rel="stylesheet" href="https://fonts.googleapis.com/css2?family=Lato:wght@400;700;900&family=Tinos&display=swap">
<style>
  :root {
    --navy: #2a2370;
    --navy-deep: #17143f;
    --navy-light: #3a3394;
    --ink-grey: #8a8a8f;
    --paper: #ffffff;
    --backdrop: #e7e7ea;
    --mark-faint: #e4e3ee;
  }
  * { box-sizing: border-box; margin: 0; padding: 0; }
  html, body { width: 1200px; height: 900px; overflow: hidden; }
  body { background: var(--backdrop); position: relative; font-family: "Lato", sans-serif; }

  .card { position: absolute; width: 640px; height: 366px; box-shadow: 0 10px 30px rgba(0,0,0,.18); overflow: hidden; }

  /* Back of card */
  .card-back { left: 500px; top: 70px; color: var(--paper); text-align: center; }
  .card-back .backdrop-art {
    position: absolute; inset: 0;
    background: radial-gradient(ellipse at 45% 30%, var(--navy-light) 0%, var(--navy) 45%, var(--navy-deep) 100%);
  }
  .card-back .mark { position: absolute; left: 50%; top: 58px; width: 92px; height: 92px; margin-left: -46px; border-radius: 50%; background: var(--paper); }
  .card-back .company { position: absolute; left: 0; right: 0; top: 182px; font-family: "Tinos", serif; font-weight: 400; font-size: 36px; letter-spacing: 1px; }
  .card-back .services { position: absolute; left: 60px; right: 60px; top: 246px; font-size: 14px; line-height: 1.6; }

  /* Front of card */
  .card-front { left: 90px; top: 450px; background: var(--paper); }
  .card-front .edge { position: absolute; left: 0; top: 0; bottom: 0; width: 8px; background: var(--navy); }
  .brand { position: absolute; left: 44px; top: 34px; display: flex; align-items: center; gap: 16px; }
  .brand .mark { width: 62px; height: 62px; border-radius: 50%; background: var(--navy); }
  .brand .company { font-family: "Tinos", serif; font-weight: 400; font-size: 31px; color: var(--navy); letter-spacing: .5px; }
  .person { position: absolute; left: 44px; top: 124px; }
  .person .name { font-weight: 900; font-size: 22px; color: var(--navy); letter-spacing: .5px; }
  .person .role { font-size: 15px; color: var(--ink-grey); }
  .contacts { position: absolute; left: 44px; top: 186px; list-style: none; font-size: 15px; line-height: 1.45; color: var(--ink-grey); }
  .contacts b { color: var(--navy); font-weight: 700; }
  .address { position: absolute; left: 44px; top: 272px; font-size: 15px; line-height: 1.3; color: var(--ink-grey); font-style: normal; }
  .address strong { display: block; color: var(--navy); font-weight: 700; }
  .watermark { position: absolute; right: 40px; bottom: 40px; text-align: right; font-family: "Tinos", serif; font-weight: 400; font-size: 30px; line-height: 1.1; color: var(--mark-faint); }
</style>
</head>
<body>
  <section class="card card-back">
    <div class="backdrop-art" role="img" aria-label="Soft abstract background of flowing light curves in deep navy tones"></div>
    <div class="mark" aria-hidden="true"></div>
    <h2 class="company">TALVANE MANAGEMENT</h2>
    <p class="services">Financial Assets Management, Proposing forming Portfolio of Assets, Consulting Service and Advising to enhance your Company's Financial Health.</p>
  </section>

  <section class="card card-front">
    <div class="edge"></div>
    <p class="watermark" aria-hidden="true">TALVANE<br>MANAGEMENT</p>
    <div class="brand">
      <div class="mark" aria-hidden="true"></div>
      <h1 class="company">TALVANE MANAGEMENT</h1>
    </div>
    <div class="person">
      <p class="name">HARUTO KISARAGI</p>
      <p class="role">CEO</p>
    </div>
    <ul class="contacts">
      <li><b>P:</b> 111 111 111</li>
      <li><b>F:</b> 222 222 222</li>
      <li><b>E:</b> haruto@talvanemanagement.jp</li>
    </ul>
    <address class="address">
      <strong>Talvane Management</strong>
      Harbor Tower, 3rd Floor,<br>Minato Street, Tokyo 12345
    </address>
  </section>
</body>
</html>
```